customer services company for the travel industry needs a flyer designed

we need a flyer for our London based company. We are an outsource service to the travel industry so our client companies receive a complaint from their customer about their holiday or travel arrangements and they pass it to us to handle. We take the stress and strain away from them that complaints present! check out our website www.fernmoorassist.co.uk - blue features as our corporate colors. The business is 26 years old so well established in the industry. The reverse of the flyer will be printed with endorsements from current company clients. I would like something light hearted projecting the relief of pressure we can provide whilst also suggesting complaints and complainants will be in professional safe capable hands

Industry/Entity Type

Travel

```html
<!DOCTYPE html>
<html lang="en">
<head>
<meta charset="utf-8">
<title>Fernmoor Assist – Flyer</title>
<link rel="stylesheet" href="https://fonts.googleapis.com/css2?family=Comfortaa:wght@300;400;700&family=Open+Sans:wght@400;600;700;800&display=swap">
<style>
  :root{
    --sky:#29b6e8;
    --sky-light:#5fcbf1;
    --sky-deep:#0e8fc9;
    --navy:#1f2f86;
    --ink:#333a40;
    --white:#ffffff;
    --page:#e9ecef;
  }
  *{box-sizing:border-box;margin:0;padding:0}
  html,body{width:1200px;height:1200px;overflow:hidden;background:var(--page)}
  body{position:relative;font-family:'Open Sans',sans-serif;color:var(--ink)}

  .flyer{position:absolute;top:95px;width:480px;height:1010px;background:var(--white);overflow:hidden;box-shadow:0 2px 6px rgba(0,0,0,.12)}
  .flyer--front{left:90px;background:var(--sky);font-family:'Comfortaa',sans-serif;color:var(--white)}
  .flyer--back{left:630px}

  /* front */
  .front-top{position:absolute;left:0;top:0;width:480px;height:260px}
  .front-top svg{position:absolute;left:0;top:0}
  .brand{position:absolute;left:30px;top:36px;width:420px}
  .brand__name{font-family:'Comfortaa',sans-serif;font-weight:300;font-size:46px;color:var(--sky-deep);letter-spacing:-.5px;line-height:1}
  .brand__tag{font-size:13px;color:#6b7a86;text-align:right;margin-top:4px;padding-right:6px}
  .art{position:absolute;border-radius:40px}
  .art--ship{left:26px;top:185px;width:170px;height:58px;background:linear-gradient(180deg,#ffffff,#cfe9f6)}
  .art--plane{left:262px;top:135px;width:120px;height:34px;background:linear-gradient(90deg,#2a6fb3,#5aa2dc)}
  .badge{position:absolute;left:330px;top:228px;width:112px;height:112px;border-radius:50%;background:var(--white);border:8px solid #d9eef9;display:flex;flex-direction:column;align-items:center;justify-content:center;color:var(--sky-deep);font-family:'Open Sans',sans-serif}
  .badge__small{font-size:10px;font-weight:700;letter-spacing:1px}
  .badge__year{font-size:30px;font-weight:800;line-height:1}

  .partners{position:absolute;left:38px;top:280px}
  .partners h2{font-size:19px;font-weight:700;margin-bottom:6px}
  .partners li{list-style:none;font-size:16px;line-height:22px;display:flex;align-items:center;gap:12px}
  .partners svg{flex:none}
  .rule{position:absolute;left:30px;width:420px;height:2px;background:rgba(255,255,255,.85)}
  .intro{position:absolute;left:36px;top:462px;width:410px;font-size:15px;line-height:20px;text-align:justify}
  .services{position:absolute;left:30px;top:548px;width:420px;text-align:center;font-size:14px;line-height:20px}
  .offer{position:absolute;left:0;top:620px;width:480px;height:64px;background:var(--white);color:var(--navy);font-family:'Open Sans',sans-serif;font-weight:800;font-size:15px;line-height:20px;text-align:center;padding-top:12px}
  .photos{position:absolute;left:0;top:684px;width:480px;height:196px;display:flex}
  .photo{flex:1}
  .photo--ship{background:linear-gradient(180deg,#a9d8f2,#3a8fcf 70%,#1b5fa3)}
  .photo--plane{background:linear-gradient(180deg,#6fb2e6,#cfe7f7)}
  .front-foot{position:absolute;left:0;top:880px;width:480px;height:130px;text-align:center;padding-top:24px}
  .front-foot__web{font-size:22px;font-weight:700}
  .front-foot__tel{font-family:'Open Sans',sans-serif;font-size:30px;font-weight:700;margin-top:8px}

  /* back */
  .back-inner{position:absolute;left:30px;top:26px;width:420px}
  .back-title{font-weight:800;font-size:18px;color:var(--sky-deep);text-align:center;margin-bottom:10px}
  .quote{border-bottom:2px solid var(--sky);padding:8px 0 10px;font-size:12.5px;line-height:17px}
  .quote p{text-align:justify}
  .quote p::before,.quote p::after{color:var(--sky);font-weight:800;font-size:16px}
  .quote p::before{content:"\201C  "}
  .quote p::after{content:" \201D"}
  .quote__name{font-weight:700;font-size:11.5px;text-transform:uppercase;margin-top:6px}
  .quote__role{font-size:11.5px;line-height:15px}
  .back-brand{margin-top:14px;text-align:center}
  .back-brand .brand__name{font-size:40px}
  .back-brand .brand__tag{text-align:center;padding:0}
  .contact{text-align:center;font-size:14px;line-height:19px;margin-top:10px}
  .contact__tel{font-weight:800;font-size:19px;margin-top:4px}
  .back-foot{position:absolute;left:0;bottom:0;width:480px;height:50px;background:var(--sky);color:var(--white);font-weight:700;font-size:20px;text-align:center;line-height:50px}
</style>
</head>
<body>

<section class="flyer flyer--front">
  <div class="front-top">
    <svg width="480" height="260" viewBox="0 0 480 260" aria-hidden="true">
      <path d="M0 0H480V150C380 205 250 235 0 215Z" fill="#ffffff"/>
      <path d="M0 215C250 235 380 205 480 150" fill="none" stroke="#bfe6f7" stroke-width="3"/>
    </svg>
    <div class="brand">
      <div class="brand__name">Fernmoor Assist</div>
      <div class="brand__tag">Customer Service &amp; Training Specialists</div>
    </div>
    <div class="art art--plane" role="img" aria-label="Illustration of a passenger jet in flight"></div>
    <div class="art art--ship" role="img" aria-label="Illustration of a white cruise ship"></div>
  </div>

  <div class="badge">
    <span class="badge__small">ESTABLISHED</span>
    <span class="badge__year">1988</span>
  </div>

  <div class="partners">
    <h2>We work with:</h2>
    <ul>
      <li><svg width="12" height="12" viewBox="0 0 12 12"><path d="M1 6l3.5 3.5L11 2" fill="none" stroke="#fff" stroke-width="2"/></svg>Tour operators</li>
      <li><svg width="12" height="12" viewBox="0 0 12 12"><path d="M1 6l3.5 3.5L11 2" fill="none" stroke="#fff" stroke-width="2"/></svg>Travel agents</li>
      <li><svg width="12" height="12" viewBox="0 0 12 12"><path d="M1 6l3.5 3.5L11 2" fill="none" stroke="#fff" stroke-width="2"/></svg>Bed banks</li>
      <li><svg width="12" height="12" viewBox="0 0 12 12"><path d="M1 6l3.5 3.5L11 2" fill="none" stroke="#fff" stroke-width="2"/></svg>Cruise lines</li>
      <li><svg width="12" height="12" viewBox="0 0 12 12"><path d="M1 6l3.5 3.5L11 2" fill="none" stroke="#fff" stroke-width="2"/></svg>Coach companies</li>
      <li><svg width="12" height="12" viewBox="0 0 12 12"><path d="M1 6l3.5 3.5L11 2" fill="none" stroke="#fff" stroke-width="2"/></svg>Airlines and dynamic packaging agents</li>
    </ul>
  </div>

  <div class="rule" style="top:450px"></div>
  <p class="intro">Our professional, experienced team manage customer service issues and complaints for travel companies serving the UK markets.</p>
  <div class="rule" style="top:538px"></div>
  <p class="services">Full outsourcing • Peak time support<br>Individual complaint handling<br>Ad hoc support • Up to date reporting</p>

  <div class="offer">Complaints management service<br>Customer service training courses for the travel industry</div>
  <div class="photos">
    <div class="photo photo--ship" role="img" aria-label="Photo of a cruise ship on blue sea"></div>
    <div class="photo photo--plane" role="img" aria-label="Photo of a jet airliner against a blue sky"></div>
  </div>

  <div class="front-foot">
    <div class="front-foot__web">www.fernmoorassist.co.uk</div>
    <div class="front-foot__tel">0207 555 0148</div>
  </div>
</section>

<section class="flyer flyer--back">
  <div class="back-inner">
    <h1 class="back-title">OUR HARD EARNED REPUTATION</h1>

    <div class="quote">
      <p>Our members have made use of and appreciated the knowledge and experience of the team at Fernmoor Assist over many years. The training courses provided by Elena for GSTF always receive very good reviews.</p>
      <div class="quote__name">Maria Holt</div>
      <div class="quote__role">Partnership and Events Manager<br>Guild of Small Tour Firms</div>
    </div>

    <div class="quote">
      <p>It is great to have the support of Ruth and her colleagues when the going gets rough. Happily we do not have to call upon them often but we have received excellent service from them over the years when we have needed help. We are happy to endorse Fernmoor Assist.</p>
      <div class="quote__name">Clara Wynn</div>
      <div class="quote__role">Northern Trails</div>
    </div>

    <div class="quote">
      <p>We have found the experience and knowledge of the team at Fernmoor Assist invaluable with the more complex claims that arise from time to time.</p>
      <div class="quote__name">Daniel Ashby</div>
      <div class="quote__role">Head of Customer Support<br>Bright Travel</div>
    </div>

    <div class="quote">
      <p>We have worked with Fernmoor Assist for a number of years. The advice received has been excellent and their knowledge and experience are second to none. We would not hesitate to recommend their services as the company has proved an invaluable resource to us.</p>
      <div class="quote__name">Sarah Pryce</div>
      <div class="quote__role">Managing Director<br>Alpine Lodge Co</div>
    </div>

    <div class="quote">
      <p>We have been delighted with the access we have to such knowledgeable and friendly support. I have no hesitation in recommending Fernmoor Assist.</p>
      <div class="quote__name">Anna Marsh</div>
      <div class="quote__role">Managing Director<br>Sunbay Villas</div>
    </div>

    <div class="back-brand">
      <div class="brand__name">Fernmoor Assist</div>
      <div class="brand__tag">Customer Service &amp; Training Specialists</div>
    </div>
    <div class="contact">
      2-6 Linden Yard<br>48 Harcourt Road<br>London N7 0QA<br>email: custserv@fernmoorassist.co.uk
      <div class="contact__tel">Tel: 0207 555 0148</div>
    </div>
  </div>
  <div class="back-foot">www.fernmoorassist.co.uk</div>
</section>

</body>
</html>
```